Brindle Studios First Business Card

I'm a real estate photographer in Maryland who also does 3D scans, walk through videos and use a drone for pictures and video as well. I have my drone license to fly commercially. I need a business card for my small business. I was thinking of just the dark logo on one side and contact/business info on the other but open to other creative ideas.
Target Market(s)
Real estate agents in Maryland
Industry/Entity Type
Real Estate
Contact Information for Business Card
Name: Marcus Pellingham, Position: Photographer and Owner, Email: marcus@brindlestudios.example, Website: brindlestudios.example, Phone: 301-555-0148

```html
<!DOCTYPE html>
<html lang="en">
<head>
<meta charset="utf-8">
<title>Brindle Studios – Business Card</title>
<link href="https://fonts.googleapis.com/css2?family=Montserrat:wght@300;400;700&display=swap" rel="stylesheet">
<style>
  :root {
    --stage: #232323;
    --card: #161616;
    --rose-gold: #e9c6aa;
    --silver: #a3a3a3;
    --ink-light: #f2f2f2;
    --card-w: 560px;
    --card-h: 320px;
  }
  * { box-sizing: border-box; margin: 0; padding: 0; }
  html, body {
    width: 1200px;
    height: 780px;
    overflow: hidden;
    background: var(--stage);
    font-family: "Montserrat", sans-serif;
  }
  .card-set {
    width: 1200px;
    height: 780px;
    display: flex;
    align-items: center;
    justify-content: center;
    gap: 40px;
  }
  .card {
    width: var(--card-w);
    height: var(--card-h);
    background: var(--card);
    border: 2px solid var(--rose-gold);
    border-radius: 24px;
    position: relative;
    overflow: hidden;
  }

  /* Front */
  .card--front {
    display: flex;
    align-items: center;
    justify-content: center;
  }
  .wordmark {
    font-weight: 300;
    letter-spacing: 0.04em;
    text-transform: uppercase;
    white-space: nowrap;
  }
  .card--front .wordmark {
    font-size: 46px;
    color: var(--silver);
  }

  /* Back */
  .card--back {
    display: grid;
    grid-template-columns: 1fr 1px 1fr;
    align-items: center;
    padding: 0 34px 0 34px;
  }
  .card--back .wordmark {
    font-size: 24px;
    color: var(--rose-gold);
    justify-self: center;
  }
  .divider {
    width: 1px;
    height: 150px;
    background: var(--rose-gold);
  }
  .contact {
    padding-left: 26px;
  }
  .contact__name {
    font-weight: 700;
    font-size: 19px;
    color: var(--rose-gold);
    line-height: 1.2;
  }
  .contact__role {
    font-weight: 400;
    font-size: 12.5px;
    color: var(--ink-light);
    margin-top: 4px;
  }
  .contact__list {
    list-style: none;
    margin-top: 22px;
    display: flex;
    flex-direction: column;
    gap: 7px;
  }
  .contact__item {
    display: flex;
    align-items: center;
    gap: 8px;
    font-size: 11.5px;
    color: var(--ink-light);
    white-space: nowrap;
  }
  .contact__icon {
    width: 11px;
    height: 11px;
    flex: none;
    fill: var(--rose-gold);
  }
</style>
</head>
<body>
  <main class="card-set">
    <section class="card card--front" aria-label="Card front">
      <span class="wordmark">Brindle Studios</span>
    </section>

    <section class="card card--back" aria-label="Card back">
      <span class="wordmark">Brindle Studios</span>
      <span class="divider"></span>
      <div class="contact">
        <h1 class="contact__name">Marcus Pellingham</h1>
        <p class="contact__role">Photographer and Owner</p>
        <ul class="contact__list">
          <li class="contact__item">
            <svg class="contact__icon" viewBox="0 0 24 24" aria-hidden="true"><path d="M2 8c0-3 4-5 10-5s10 2 10 5v2h-6V7.5c-1.5-.5-6.5-.5-8 0V10H2z"/><path d="M5 12h14l2 9H3z"/></svg>
            301-555-0148
          </li>
          <li class="contact__item">
            <svg class="contact__icon" viewBox="0 0 24 24" aria-hidden="true"><path d="M2 5h20v2l-10 6L2 7z"/><path d="M2 9.5l10 6 10-6V19H2z"/></svg>
            marcus@brindlestudios.example
          </li>
          <li class="contact__item">
            <svg class="contact__icon" viewBox="0 0 24 24" aria-hidden="true"><circle cx="12" cy="12" r="10"/></svg>
            brindlestudios.example
          </li>
        </ul>
      </div>
    </section>
  </main>
</body>
</html>
```